Letterhead Design Project

Need Letterhead and Envelpe design with One Single or Both Side pockets for a yong dynamic employee friendly IT services company. It should be professional and sleek and should look fresh.

Target Market(s)

IT Corporate

Industry/Entity Type

It Company

```html
<!DOCTYPE html>
<html lang="en">
<head>
<meta charset="utf-8">
<title>Letterhead</title>
<link rel="stylesheet" href="https://fonts.googleapis.com/css2?family=Jura:wght@400&family=Outfit:wght@500&display=swap">
<style>
  :root {
    --teal-deep: #00858c;
    --teal-bright: #00a6b0;
    --red-deep: #a3272d;
    --red-bright: #e2333a;
    --logo-dot: #52e6ef;
    --paper: #ffffff;
    --footer-ink: #555a5e;
    --logo-ink: #ffffff;
  }
  html, body {
    margin: 0;
    padding: 0;
    overflow: hidden;
    background: var(--paper);
  }
  .letterhead {
    position: relative;
    width: 862px;
    height: 1200px;
    overflow: hidden;
    background: var(--paper);
  }
  .letterhead__shapes {
    position: absolute;
    inset: 0;
  }
  .brand {
    position: absolute;
    left: 544px;
    top: 114px;
    display: flex;
    align-items: center;
    gap: 10px;
  }
  .brand__dot {
    width: 68px;
    height: 68px;
    border-radius: 50%;
    background: var(--logo-dot);
  }
  .brand__name {
    font-family: "Outfit", sans-serif;
    font-weight: 500;
    font-size: 28px;
    color: var(--logo-ink);
    letter-spacing: 0.2px;
    padding-top: 30px;
  }
  .contact {
    position: absolute;
    left: 201px;
    top: 1109px;
    margin: 0;
    font-family: "Jura", sans-serif;
    font-size: 14.5px;
    line-height: 21.5px;
    color: var(--footer-ink);
    font-style: normal;
    letter-spacing: 0.3px;
  }
</style>
</head>
<body>
<main class="letterhead">
  <svg class="letterhead__shapes" width="862" height="1200" viewBox="0 0 862 1200" aria-hidden="true">
    <defs>
      <linearGradient id="header-fill" x1="0" y1="0" x2="1" y2="1">
        <stop offset="0" stop-color="var(--teal-deep)"/>
        <stop offset="1" stop-color="var(--teal-bright)"/>
      </linearGradient>
      <linearGradient id="accent-fill" x1="0" y1="0" x2="0.3" y2="1">
        <stop offset="0" stop-color="var(--red-deep)"/>
        <stop offset="1" stop-color="var(--red-bright)"/>
      </linearGradient>
      <linearGradient id="corner-fill" x1="0" y1="0" x2="0.4" y2="1">
        <stop offset="0.3" stop-color="var(--teal-deep)"/>
        <stop offset="1" stop-color="var(--teal-bright)"/>
      </linearGradient>
    </defs>
    <polygon class="header-band" points="6,0 720,0 785,195 6,195" fill="url(#header-fill)"/>
    <polygon class="header-accent" points="767,0 862,0 862,280 849,238" fill="url(#accent-fill)"/>
    <polygon class="corner-wedge" points="0,742 152,1162 68,1200 6,1200" fill="url(#corner-fill)"/>
  </svg>

  <div class="brand">
    <span class="brand__dot"></span>
    <span class="brand__name">Logo here</span>
  </div>

  <address class="contact">
    Address Line 1<br>
    Tel: 00 00 0000 0000 Fax: Fax Number Here Mobile: 00 00000 00000<br>
    Email: abc@def.com Website: webaddress
  </address>
</main>
</body>
</html>
```